Medical Skincare services/menu/pricing Booklet 12 pages

We need produce a 12-page glossy, saddle-stitched booklet (5 1/2" tall X 81/2" wide). The booklet will be used as a services menu for a skin care salon. I have mocked up the booklet (w/ all copy) in WORD and I've provided a separate PDF of the accurate page order (see files attached). IMPORTANT: Feel free to use your creativity yet style-wise it should kinda match my wife's website colors and text style. Her clients are demanding so she wants a clean, high end, modern look (ala Apple maybe?). See her website for a frame of reference www.GlowWithMira.com

Target Market(s)

upscale female, professional women, teens with acne

Industry/Entity Type

Medical

Requirements
Must have
• the pics in the mock up are important. I've attached them here

```html
<!DOCTYPE html>
<html lang="en">
<head>
<meta charset="utf-8">
<title>Glow With Mira – Service Booklet Presentation</title>
<link href="https://fonts.googleapis.com/css2?family=Lato:wght@400;700;900&display=swap" rel="stylesheet">
<style>
  :root{
    --board:#c2c2c2;
    --ink:#000;
    --paper:#fff;
    --silver:#cfcfcf;
    --text:#3a3a3a;
    --photo-a:#8a7a6a;
    --photo-b:#c8c2b6;
    --dress-a:#6f8c93;
  }
  *{margin:0;padding:0;box-sizing:border-box}
  html,body{width:1200px;height:1200px;overflow:hidden;background:var(--board);font-family:'Lato',sans-serif}
  .board{position:relative;width:1200px;height:1200px}
  .label{position:absolute;font-weight:900;font-size:29px;color:var(--ink);transform:translateX(-50%);letter-spacing:.5px}
  .panel{position:absolute;overflow:hidden;box-shadow:2px 3px 6px rgba(0,0,0,.35)}

  /* Front cover */
  .front{left:39px;top:268px;width:536px;height:349px;background:var(--ink)}
  .brand-name{position:absolute;left:0;right:0;top:76px;text-align:center;font-family:'Lato',sans-serif;font-weight:900;font-size:46px;line-height:48px;color:var(--silver);letter-spacing:1px}
  .tag{position:absolute;height:22px;font-size:13px;line-height:20px;text-align:center;white-space:nowrap}
  .tag.solid{background:var(--paper);color:var(--ink);border:1px solid var(--paper)}
  .tag.outline{color:var(--paper);border:1px solid #bbb}
  .front-url{position:absolute;left:0;right:0;top:313px;text-align:center;color:#ddd;font-size:10.5px;letter-spacing:3.2px}
  .front-url-line{position:absolute;left:210px;width:116px;top:332px;height:2px;background:linear-gradient(90deg,transparent,#fff,transparent)}

  /* Inside spread */
  .inside{left:622px;top:268px;width:536px;height:349px;background:var(--paper)}
  .inside-strip{position:absolute;left:0;top:0;width:71px;height:100%;background:var(--ink)}
  .inside-photo{position:absolute;left:71px;top:0;width:155px;height:100%;background:linear-gradient(90deg,var(--photo-a),var(--photo-b) 55%,var(--dress-a))}
  .bio{position:absolute;left:281px;width:226px;color:var(--text)}
  .bio h2{font-size:10px;font-weight:700;color:#111;text-align:center;margin-bottom:6px}
  .bio p{font-size:7.6px;line-height:10.6px;text-align:justify;text-align-last:center}

  /* Back cover */
  .back{left:330px;top:683px;width:540px;height:351px;background:var(--paper)}
  .back-block{position:absolute;left:8px;top:135px;width:304px;height:211px;background:var(--ink)}
  .back-photo-frame{position:absolute;left:28px;top:12px;width:264px;height:228px;background:var(--paper)}
  .back-photo{position:absolute;left:34px;top:17px;width:252px;height:216px;background:radial-gradient(ellipse at 45% 45%,#6b5040,#9c9590 55%,#dcd8d2)}
  .back-brand{position:absolute;left:8px;width:304px;top:280px;text-align:center;font-family:'Lato',sans-serif;font-weight:900;font-size:24px;line-height:28px;color:var(--silver);letter-spacing:.5px}
  .contact{position:absolute;left:336px;width:180px;text-align:center;color:#111}
  .icon{position:absolute;left:416px;width:21px;height:21px}
  .c-head{font-size:10.5px;line-height:12px;font-weight:900}
  .c-sub{font-size:8px;line-height:10.5px}
  .hours{position:absolute;left:350px;top:243px;width:185px;font-size:8.2px;color:#222}
  .hours .row{position:relative;height:16px}
  .hours .day{position:absolute;left:0}
  .hours .rule{position:absolute;left:45px;width:51px;top:6px;height:1px;background:#222}
  .hours .time{position:absolute;left:105px}
</style>
</head>
<body>
<div class="board">
  <div class="label" style="left:290px;top:210px">FRONT</div>
  <div class="label" style="left:886px;top:210px">INSIDE</div>
  <div class="label" style="left:600px;top:1074px">BACK</div>

  <!-- Front cover -->
  <section class="panel front">
    <div class="brand-name">GLOW WITH MIRA</div>
    <div class="tag solid" style="left:113px;top:196px;width:104px">HydraGlow Facial</div>
    <div class="tag solid" style="left:222px;top:196px;width:89px">Laser Renew</div>
    <div class="tag solid" style="left:317px;top:196px;width:105px">IPL (BrightLight)</div>
    <div class="tag outline" style="left:97px;top:234px;width:93px">Vascular</div>
    <div class="tag solid" style="left:201px;top:234px;width:115px">Microneedling Pro</div>
    <div class="tag outline" style="left:326px;top:234px;width:121px">LED Light Therapy</div>
    <div class="tag solid" style="left:88px;top:270px;width:66px">Vita Peel</div>
    <div class="tag outline" style="left:159px;top:270px;width:191px">Customized Facials &amp; Peels</div>
    <div class="tag solid" style="left:356px;top:270px;width:104px">Dermaplane</div>
    <div class="front-url">glowwithmira.com</div>
    <div class="front-url-line"></div>
  </section>

  <!-- Inside spread -->
  <section class="panel inside">
    <div class="inside-strip"></div>
    <div class="inside-photo" role="img" aria-label="Full-length photo of the aesthetician in a patterned blue maxi dress beside a flower planter"></div>
    <div class="bio" style="top:37px">
      <h2>Mira Castell Medical Aesthetician &amp; Owner</h2>
      <p>As a teenager, I had cystic acne so bad that I would ditch school to swim in the ocean because the salt water seemed to dry out and heal my skin. I was on such a mission to clear my skin that I spent my weekly allowance on skin care products I saw on TV. Then, I memorized every ingredient. I was so intrigued by the beauty industry that, by 19, I began a career as a make up artist for Lumière, Velour, Brightline, Prisma, and Stella Rae. By 23, I was a skincare consultant for the Marguerite Vale Salons in Beverly Hills and Orange County California. I was honored to learn from the world's most demanding clients.</p>
    </div>
    <div class="bio" style="top:194px">
      <h2>I Understand Why Your Skin Matters</h2>
      <p>Admit it. We take more pictures of ourselves than ever...and then try to "fix" our blemishes with photo filters. I understand your frustrations. Some of you know I've had a parallel career as a professional singer with dozens of network TV appearances; where the HD cameras take extreme close ups...Yikes!). I also sing the National Anthem at pro football, basketball, and baseball games, where their 200 foot-wide Jumbo-Tron screens constantly remind me that skin imperfections are magnified. I will help get your skin more naturally beautiful so you can use less photo filters ;-)</p>
    </div>
  </section>

  <!-- Back cover -->
  <section class="panel back">
    <div class="back-block"></div>
    <div class="back-photo-frame"></div>
    <div class="back-photo" role="img" aria-label="Portrait of the aesthetician in a grey fur-trimmed sweater over a faded collage of event photos"></div>
    <div class="back-brand">GLOW WITH MIRA</div>

    <svg class="icon" style="top:15px" viewBox="0 0 21 21"><circle cx="10.5" cy="10.5" r="10.5" fill="#000"/><rect x="5.5" y="6.5" width="10" height="8" rx="1" fill="none" stroke="#fff" stroke-width="1.3"/><line x1="5.5" y1="9" x2="15.5" y2="9" stroke="#fff" stroke-width="1.3"/></svg>
    <div class="contact c-head" style="top:42px">BOOK ONLINE</div>
    <div class="contact c-sub" style="top:60px">www.GlowWithMira.com</div>

    <svg class="icon" style="top:76px" viewBox="0 0 21 21"><circle cx="10.5" cy="10.5" r="10.5" fill="#000"/><path d="M7 5.5c-1 .5-1.5 1.5-1 3 1 3 3.5 5.5 6.5 6.5 1.5.5 2.5 0 3-1l-2-2-1.3.8c-1.3-.7-2.3-1.7-3-3L10 8.5z" fill="#fff"/></svg>
    <div class="contact c-head" style="top:103px">Or Call/Text</div>
    <div class="contact c-sub" style="top:122px">(720) 555-0148</div>

    <svg class="icon" style="top:141px" viewBox="0 0 21 21"><circle cx="10.5" cy="10.5" r="10.5" fill="#000"/><path d="M10.5 4.5a4 4 0 0 0-4 4c0 3 4 8 4 8s4-5 4-8a4 4 0 0 0-4-4z" fill="#fff"/><circle cx="10.5" cy="8.5" r="1.5" fill="#000"/></svg>
    <div class="contact c-head" style="top:171px">LOCATION:</div>
    <div class="contact c-sub" style="top:188px">Glow With Mira<br>4120 Alder Ave #200<br>Lone Tree, Colorado 80124</div>
    <div class="contact c-head" style="top:227px">BY APPT. HOURS</div>

    <div class="hours">
      <div class="row"><span class="day">Monday</span><span class="rule"></span><span class="time">10:00am-4:00pm</span></div>
      <div class="row"><span class="day">Tuesday</span><span class="rule"></span><span class="time">10:00am-6:00pm</span></div>
      <div class="row"><span class="day">Thursday</span><span class="rule"></span><span class="time">10:00am-6:00pm</span></div>
      <div class="row"><span class="day">Friday</span><span class="rule"></span><span class="time">10:00pm-6:00pm</span></div>
      <div class="row"><span class="day">Saturday</span><span class="rule"></span><span class="time">10:00-am-4:00pm</span></div>
      <div class="row"><span class="day">Sunday</span><span class="rule"></span><span class="time">Closed</span></div>
    </div>
  </section>
</div>
</body>
</html>
```